Life Coach for Lawyers Business Card Design

Elegant, original, business card design for life coaching service for associate attorneys who work in big law and struggle with stress, overwhelm, and time management. Double sided design.

Target Market(s)

Women associate attorneys who work in big law and struggle with stress, overwhelm, and time management.

Industry/Entity Type

Life Coaching

Contact Information for Business Card

Marlene Quorthby
Life Coach
519.607.4431
brightcounselpath.net
marlene@brightcounselpath.net
@brightcounselpath (Instagram)

Font styles to use
Other font styles liked:
• Silver South font duo. See uploaded files.

Requirements
Must have
• Icons for phone, website, email, and Instagram instead of words. Specific colors used in my logo (171B2B, 421121, FFFFFF)
Nice to have
• Foil. Embossed. Feminine design.
Should not have
• Any colors other than those used in logo. See uploaded files.

```html
<!DOCTYPE html>
<html lang="en">
<head>
<meta charset="utf-8">
<title>Bright Counsel Path — Business Card</title>
<link rel="stylesheet" href="https://fonts.googleapis.com/css2?family=Bodoni+Moda:wght@400;500&display=swap">
<style>
  :root {
    --wine: #421121;
    --navy: #171B2B;
    --white: #FFFFFF;
    --stage: #2a2a2c;
    --ring: rgba(255, 255, 255, 0.75);
  }
  * { box-sizing: border-box; margin: 0; padding: 0; }
  html, body {
    width: 1200px;
    height: 880px;
    overflow: hidden;
    background: var(--stage);
    font-family: "Bodoni Moda", "Times New Roman", serif;
  }
  .stage {
    width: 1200px;
    height: 880px;
    display: flex;
    flex-direction: column;
    align-items: center;
    justify-content: center;
    gap: 56px;
  }
  .card {
    width: 560px;
    height: 320px;
    border-radius: 18px;
    position: relative;
    overflow: hidden;
    box-shadow: 0 14px 30px rgba(0, 0, 0, 0.45);
  }

  /* Back side */
  .card-back {
    background: var(--wine);
    display: flex;
    align-items: center;
    justify-content: center;
  }
  .brand-seal {
    width: 170px;
    height: 170px;
    border-radius: 50%;
    border: 1px solid var(--ring);
    display: flex;
    align-items: center;
    justify-content: center;
    text-align: center;
  }
  .brand-seal-name {
    color: var(--white);
    font-size: 19px;
    font-weight: 400;
    letter-spacing: 2px;
    line-height: 1.35;
    text-transform: uppercase;
  }

  /* Front side */
  .card-front {
    background: var(--white);
  }
  .brand-wordmark {
    position: absolute;
    top: 62px;
    left: 0;
    right: 0;
    text-align: center;
    color: var(--wine);
    font-size: 38px;
    font-weight: 400;
    letter-spacing: 4px;
    text-transform: uppercase;
    line-height: 1;
  }
  .info {
    position: absolute;
    top: 158px;
    left: 60px;
    right: 40px;
    display: flex;
    align-items: center;
  }
  .person {
    width: 200px;
    text-align: right;
    padding-right: 22px;
    padding-top: 30px;
  }
  .person-name {
    color: var(--wine);
    font-size: 17px;
    font-variant: small-caps;
    letter-spacing: 1px;
  }
  .person-role {
    color: var(--navy);
    font-size: 13px;
    margin-top: 2px;
  }
  .divider {
    width: 1px;
    height: 96px;
    background: var(--wine);
  }
  .contact-list {
    list-style: none;
    padding-left: 20px;
    color: var(--navy);
    font-size: 13px;
    line-height: 1.75;
  }
  .contact-list li {
    display: flex;
    align-items: center;
    gap: 10px;
  }
  .contact-icon {
    width: 13px;
    height: 13px;
    flex: none;
    fill: var(--navy);
  }
  .edge-band {
    position: absolute;
    left: 0;
    right: 0;
    bottom: 0;
    height: 9px;
    display: flex;
  }
  .edge-band-wine { flex: 0 0 60%; background: var(--wine); }
  .edge-band-navy { flex: 1; background: var(--navy); }
</style>
</head>
<body>
<main class="stage">

  <section class="card card-back" aria-label="Card back">
    <div class="brand-seal">
      <p class="brand-seal-name">Bright<br>Counsel<br>Path</p>
    </div>
  </section>

  <section class="card card-front" aria-label="Card front">
    <h1 class="brand-wordmark">Bright Counsel Path</h1>

    <div class="info">
      <div class="person">
        <p class="person-name">Marlene Quorthby</p>
        <p class="person-role">Life Coach</p>
      </div>
      <div class="divider"></div>
      <ul class="contact-list">
        <li>
          <svg class="contact-icon" viewBox="0 0 24 24" aria-hidden="true"><path d="M6.6 10.8c1.4 2.8 3.8 5.1 6.6 6.6l2.2-2.2c.3-.3.7-.4 1-.2 1.1.4 2.3.6 3.6.6.6 0 1 .4 1 1V20c0 .6-.4 1-1 1C10.6 21 3 13.4 3 4c0-.6.4-1 1-1h3.5c.6 0 1 .4 1 1 0 1.3.2 2.5.6 3.6.1.3 0 .7-.2 1z"/></svg>
          <span>519.607.4431</span>
        </li>
        <li>
          <svg class="contact-icon" viewBox="0 0 24 24" aria-hidden="true"><path d="M2 5h20v14H2z M3.5 6.5 12 13l8.5-6.5" fill="none" stroke="#171B2B" stroke-width="2"/><path d="M2 5h20L12 13z"/></svg>
          <span>marlene@brightcounselpath.net</span>
        </li>
        <li>
          <svg class="contact-icon" viewBox="0 0 24 24" aria-hidden="true"><g fill="none" stroke="#171B2B" stroke-width="1.8"><circle cx="12" cy="12" r="9.5"/><ellipse cx="12" cy="12" rx="4.2" ry="9.5"/><path d="M2.5 12h19M4 7h16M4 17h16"/></g></svg>
          <span>brightcounselpath.net</span>
        </li>
        <li>
          <svg class="contact-icon" viewBox="0 0 24 24" aria-hidden="true"><rect x="3" y="3" width="18" height="18" rx="2"/></svg>
          <span>@brightcounselpath</span>
        </li>
      </ul>
    </div>

    <div class="edge-band">
      <span class="edge-band-wine"></span>
      <span class="edge-band-navy"></span>
    </div>
  </section>

</main>
</body>
</html>
```